Sales PowerPoint Template to help us attract new customers

We need to create a generic PowerPoint template for our organization. We are in the commercial facilities industry, servicing convenience, restaurants, grocery, and retail customers in the US. We handle trades such as HVAC, Refrigeration, Plumbing, Electrical, Food Equipment, Coffee, etc.

We need to incorporate our new logo, updated colors, Font (Arial). We want it to stand out in this deck and avoid looking like all other facility companies. We want to make sure the template size is not too large (less than 20 MB), so it prevent people to edit/send.
Attached are new logo, colors, old powerpoint template, and finally the "New Design to Incorporate into Template" is new materials we're looking to leverage. This might give you ideas.

Create at least 10 slides (1 cover, 1 agenda slide, at least 7 general slides, and 1 wrap-up slide)

Target Market(s)

Convenience Stores, Retail Stores, Groceries, and Restaurants in the US

Industry/Entity Type

Facilities Services (HVAC, Refrigeration, Plumbing, Electrical, etc, repair and preventative maintenance)

Font styles to use
Other font styles liked:
• Arial

Requirements
Must have
• Follow company colors and font (Arial)
Should not have
• Not approved company colors, font

```html
<!DOCTYPE html>
<html lang="en">
<head>
<meta charset="utf-8">
<title>Norvane Facility Solutions – PACE System Cover</title>
<link rel="stylesheet" href="https://fonts.googleapis.com/css2?family=Archivo:wght@400;500;800;900&family=Arimo:wght@400&display=swap">
<style>
  :root {
    --cream: #efefe0;
    --cream-light: #f8f8f1;
    --olive: #8a9a2f;
    --olive-dark: #7c8b2b;
    --amber: #f5a300;
    --white: #ffffff;
    --photo-warm: #b9a58e;
    --photo-cool: #5f6268;
  }
  html, body {
    margin: 0;
    padding: 0;
    overflow: hidden;
    background: var(--white);
  }
  .slide {
    position: relative;
    width: 1200px;
    height: 674px;
    overflow: hidden;
    background: linear-gradient(100deg, var(--cream-light) 0%, var(--cream) 60%, #e9ead6 100%);
    font-family: "Arimo", Arial, sans-serif;
  }
  .hero-photo {
    position: absolute;
    inset: 0;
    width: 1200px;
    height: 674px;
  }
  .headline-panel {
    position: absolute;
    left: 94px;
    top: 178px;
    width: 541px;
    height: 361px;
    background: var(--olive);
    border-radius: 27px;
  }
  .headline-kicker,
  .headline-main {
    position: absolute;
    left: 45px;
    margin: 0;
    font-family: "Archivo", Arial, sans-serif;
    font-weight: 900;
    letter-spacing: -1.5px;
    text-transform: uppercase;
    line-height: 1;
  }
  .headline-kicker {
    top: 84px;
    font-size: 37px;
    color: var(--amber);
  }
  .headline-main {
    top: 121px;
    font-size: 51px;
    line-height: 50px;
    color: var(--white);
  }
  .headline-sub {
    position: absolute;
    left: 45px;
    top: 225px;
    margin: 0;
    font-size: 40px;
    line-height: 48px;
    color: var(--white);
    font-weight: 400;
  }
  .brand-card {
    position: absolute;
    left: 603px;
    top: 476px;
    width: 328px;
    height: 135px;
    background: var(--white);
    border-radius: 13px;
  }
  .brand-name {
    position: absolute;
    left: 24px;
    top: 26px;
    display: flex;
    align-items: center;
    gap: 14px;
    font-family: "Archivo", Arial, sans-serif;
    font-weight: 500;
    font-size: 40px;
    letter-spacing: 5px;
    color: var(--olive-dark);
    line-height: 1;
  }
  .brand-name .brand-square {
    width: 30px;
    height: 30px;
    background: var(--olive-dark);
  }
  .brand-tagline {
    position: absolute;
    right: 30px;
    top: 90px;
    font-family: "Archivo", Arial, sans-serif;
    font-weight: 500;
    font-size: 20px;
    letter-spacing: 0.5px;
    color: var(--olive-dark);
  }
</style>
</head>
<body>
  <main class="slide">
    <svg class="hero-photo" viewBox="0 0 1200 674" role="img" aria-label="Photo of shoppers at a grocery store checkout with a shopping cart and groceries">
      <defs>
        <linearGradient id="photoTone" x1="0" y1="0" x2="1" y2="1">
          <stop offset="0" stop-color="#3e4147"/>
          <stop offset="0.35" stop-color="#a6948a"/>
          <stop offset="0.65" stop-color="var(--photo-warm)"/>
          <stop offset="1" stop-color="var(--photo-cool)"/>
        </linearGradient>
      </defs>
      <path d="M322 60 H1200 V674 H557 L376 154 H274 V108 Q274 60 322 60 Z" fill="url(#photoTone)"/>
    </svg>

    <section class="headline-panel">
      <p class="headline-kicker">Using our</p>
      <h1 class="headline-main">Patented PACE<br>System</h1>
      <p class="headline-sub">To Help Save You<br>Money On Maintenance</p>
    </section>

    <div class="brand-card">
      <div class="brand-name"><span class="brand-square"></span>NORVANE</div>
      <div class="brand-tagline">Facility Solutions</div>
    </div>
  </main>
</body>
</html>
```